Business Card Design

I am a Special Event Consultant,I arrange and organise Special Events - Product Launches,Sponsorship and Product Displays.

I would like the RTV to be a feature of the design with 'Special Event Services" underneath - keep it very simple but creative using this information. So it is just the letters "RTV" with Event Services underneath.

(Simple Colours - Silver, Black, Grey - no bright colours - We work for Valtoria Drenn,KDX, Lyndrel So it is class and classic.)

Only my Name and mobile on the front.

Contact Information for Business Card

FRONT
Tess Varnholt
Tel: 0436 218907

BACK
Email: tess@rtveventservices.example.au

2807 Wexbury Heights,83 Pollard Street
NORTHVALE.Vic.3158.

```html
<!DOCTYPE html>
<html lang="en">
<head>
<meta charset="utf-8">
<title>RTV Special Event Services – Business Card</title>
<link rel="stylesheet" href="https://fonts.googleapis.com/css2?family=Crimson+Pro:wght@400&display=swap">
<style>
  :root {
    --card-centre: #ffffff;
    --card-mid: #e9e9e9;
    --card-edge: #b6b6b6;
    --label-blue: #25609c;
    --text-grey: #5a5a5a;
    --mark-charcoal: #3f3f3f;
  }
  * { margin: 0; padding: 0; box-sizing: border-box; }
  html, body {
    width: 1200px;
    height: 741px;
    overflow: hidden;
    background: var(--card-edge);
  }
  .card {
    position: relative;
    width: 1200px;
    height: 741px;
    overflow: hidden;
    background: radial-gradient(ellipse 56% 66% at 50% 52%,
      var(--card-centre) 0%, var(--card-centre) 58%, var(--card-mid) 80%, var(--card-edge) 100%);
    font-family: "Crimson Pro", "Times New Roman", serif;
    font-weight: 400;
    color: var(--text-grey);
  }
  .contact-line {
    position: absolute;
    white-space: nowrap;
    line-height: 1;
  }
  .contact-label {
    color: var(--label-blue);
    text-decoration: underline;
    text-decoration-thickness: 2px;
    text-underline-offset: 9px;
  }
  .contact-name {
    left: 48px;
    top: 48px;
    font-size: 41px;
    letter-spacing: 0.16em;
  }
  .contact-phone {
    right: 46px;
    top: 650px;
    font-size: 49px;
    letter-spacing: 0.08em;
  }
  .brand {
    position: absolute;
    left: 0;
    width: 100%;
    text-align: center;
    line-height: 1;
    white-space: nowrap;
  }
  .brand-name {
    top: 286px;
    font-size: 140px;
    letter-spacing: 0.14em;
    padding-left: 0.14em;
    color: var(--mark-charcoal);
  }
  .brand-tagline {
    top: 433px;
    font-size: 50px;
    letter-spacing: 0.22em;
    padding-left: 0.22em;
    color: var(--text-grey);
  }
</style>
</head>
<body>
  <main class="card">
    <p class="contact-line contact-name"><span class="contact-label">NAME :</span> TESS VARNHOLT</p>
    <div class="brand brand-name">RTV</div>
    <div class="brand brand-tagline">SPECIAL EVENT SERVICES</div>
    <p class="contact-line contact-phone"><span class="contact-label">TEL:</span> 0436 218907</p>
  </main>
</body>
</html>
```